KEV.PRO- Darren Holcombe Fitness- needs a clever business card using the logo, name, info, contact

I need a business card designed for my Online Personal Training company called KEV.PRO, abbreviation for Darren Holcombe Fitness. My company focuses on coaching in personal health and personal growth to unleash your greatest potential. I would like to see designs that use my color scheme of a redish-orange (C:0,M:84,Y:100,K:0), grey, white, black, and my company font is OSWALD. The final design should communicate some aspects of design, health, motivation, growth, in some way. The logo is very important to the company and can be displayed in any of the colors previously mentioned. Must include the company name, my website: www.kev-pro.example , my email: dan@kev-pro.example

Target Market(s)

Personal health, fitness, general public, those who lack knowledge, awareness, and confidence in personal health

Industry/Entity Type

Personal Trainer

Font styles to use
Other font styles liked:
• OSWALD. (Bold, Regular, Light)

Colors
f37122
ffffff
9d9d9d
000000

Requirements
Must have
• Must include the logo, company name, my website: www.kev-pro.example , my email: dan@kev-pro.example
Nice to have
• Variations of the colors scheme of a redish-orange (C:0,M:84,Y:100,K:0), grey, white, black. Logo, card, or text can be in any of these colors.
• Possible quote like "Take control of your personal health to unleash your greatest potential" or "Unleashing your greatness first begins with fitness of the body and mind"

```html
<!DOCTYPE html>
<html lang="en">
<head>
<meta charset="utf-8">
<title>KEV.PRO Business Card</title>
<link href="https://fonts.googleapis.com/css2?family=Oswald:wght@300;400;700&display=swap" rel="stylesheet">
<style>
  :root {
    --orange: #f0542a;
    --white: #ffffff;
    --grey: #9d9d9d;
    --black: #0d0d0d;
    --charcoal: #2b2a2a;
    --backdrop: #3a3330;
  }
  * { margin: 0; padding: 0; box-sizing: border-box; }
  html, body {
    width: 1200px; height: 716px; overflow: hidden;
    background: var(--backdrop);
    font-family: "Oswald", sans-serif;
  }
  .canvas { position: relative; width: 1200px; height: 716px; }

  .card {
    position: absolute;
    width: 540px; height: 309px;
    border-radius: 10px;
    overflow: hidden;
  }

  /* Back of card */
  .card-back {
    left: 50px; top: 90px;
    background: var(--black);
    display: flex; flex-direction: column;
    align-items: center; justify-content: center;
  }
  .card-back .brand-name {
    font-weight: 700; font-size: 44px; letter-spacing: 1px;
    color: var(--grey);
    line-height: 1;
  }
  .card-back .brand-tagline {
    margin-top: 8px;
    font-weight: 300; font-size: 11px; letter-spacing: 2px;
    color: #3e3e3e; text-transform: uppercase;
  }

  /* Front of card */
  .card-front {
    left: 610px; top: 317px;
    background: var(--charcoal);
  }
  .front-brand {
    position: absolute; left: 28px; top: 24px;
  }
  .front-brand .brand-name {
    font-weight: 700; font-size: 36px; color: var(--white); line-height: 1;
  }
  .front-brand .brand-tagline {
    font-weight: 400; font-size: 10px; color: var(--white);
    text-transform: uppercase; letter-spacing: 0.3px; margin-top: 2px;
  }
  .person {
    position: absolute; left: 28px; top: 118px;
  }
  .person .name {
    font-weight: 700; font-size: 24px; color: var(--orange);
    text-transform: uppercase; line-height: 1.1;
  }
  .person .role {
    font-weight: 300; font-size: 15px; color: var(--white);
  }
  .contacts {
    position: absolute; left: 28px; top: 196px;
    list-style: none;
  }
  .contacts li {
    display: flex; align-items: center; gap: 8px;
    font-weight: 300; font-size: 12px; color: var(--white);
    height: 20px;
  }
  .contacts svg { width: 12px; height: 12px; fill: var(--orange); }

  .mark-disc {
    position: absolute; left: 215px; top: -25px;
    width: 370px; height: 370px; border-radius: 50%;
    background: var(--white);
    display: flex; align-items: center; justify-content: center;
  }
  .mark-disc .brand-name {
    font-weight: 700; font-size: 64px; color: var(--orange);
    margin-right: 30px;
  }
</style>
</head>
<body>
<main class="canvas">

  <section class="card card-back" aria-label="Card back">
    <div class="brand-name">KEV.PRO</div>
    <div class="brand-tagline">Darren Holcombe Fitness</div>
  </section>

  <section class="card card-front" aria-label="Card front">
    <div class="mark-disc">
      <span class="brand-name">KEV.PRO</span>
    </div>

    <header class="front-brand">
      <div class="brand-name">KEV.PRO</div>
      <div class="brand-tagline">Darren Holcombe Fitness</div>
    </header>

    <div class="person">
      <div class="name">Alex Marsh</div>
      <div class="role">President</div>
    </div>

    <ul class="contacts">
      <li>
        <svg viewBox="0 0 24 24" aria-hidden="true"><path d="M6.6 10.8a15.1 15.1 0 0 0 6.6 6.6l2.2-2.2a1 1 0 0 1 1-.25 11.4 11.4 0 0 0 3.6.57 1 1 0 0 1 1 1V20a1 1 0 0 1-1 1A17 17 0 0 1 3 4a1 1 0 0 1 1-1h3.5a1 1 0 0 1 1 1c0 1.25.2 2.45.57 3.6a1 1 0 0 1-.25 1z"/></svg>
        555 010 4821
      </li>
      <li>
        <svg viewBox="0 0 24 24" aria-hidden="true"><path d="M2 5h20v14H2z M2 5l10 8 10-8" /><path d="M2 5l10 8 10-8v2l-10 8L2 7z" fill="#2b2a2a"/></svg>
        dan@kev-pro.example
      </li>
      <li>
        <svg viewBox="0 0 24 24" aria-hidden="true"><path d="M12 2a10 10 0 1 0 0 20 10 10 0 0 0 0-20zm6.9 6h-2.9a15.7 15.7 0 0 0-1.4-3.6A8 8 0 0 1 18.9 8zM12 4c.8 1.2 1.5 2.5 1.9 4h-3.8c.4-1.5 1.1-2.8 1.9-4zM4.3 14a8 8 0 0 1 0-4h3.4a16 16 0 0 0 0 4zm.8 2h2.9c.3 1.3.8 2.5 1.4 3.6A8 8 0 0 1 5.1 16zM8 8H5.1a8 8 0 0 1 4.3-3.6C8.8 5.5 8.3 6.7 8 8zm4 12c-.8-1.2-1.5-2.5-1.9-4h3.8c-.4 1.5-1.1 2.8-1.9 4zm2.3-6H9.7a14 14 0 0 1 0-4h4.6a14 14 0 0 1 0 4zm.3 5.6c.6-1.1 1.1-2.3 1.4-3.6h2.9a8 8 0 0 1-4.3 3.6zm1.7-5.6a16 16 0 0 0 0-4h3.4a8 8 0 0 1 0 4z"/></svg>
        www.kev-pro.example
      </li>
    </ul>
  </section>

</main>
</body>
</html>
```